I need a business card for my new bakery - Mill Lane Oven Co. We make biscuits, cakes, muffins and other sweets. Our food is honest, wholesome and down to earth - i'd love this to be reflected in the design of the card. The design MUST include our logo (see the attached image - which needs to be replicated). The design should only use 2 or at most 3 colours.

Industry/Entity Type

Bakery

Requirements
Must have
• Must include my logo.
Must have a clean, simple design.
Space for my name, my title, my phone number, my facebook page (I will provide details later)
Should not have
• Must not have lots of bright colours.
Must not have any unnescassry graphics.

```html
<!DOCTYPE html>
<html lang="en">
<head>
<meta charset="utf-8">
<title>Mill Lane Oven Co – Business Card</title>
<link href="https://fonts.googleapis.com/css2?family=Tinos:wght@400;700&family=Open+Sans:wght@400;600&display=swap" rel="stylesheet">
<style>
  :root {
    --page: #e8e5e1;
    --card: #ffffff;
    --brown-dark: #5a3a27;
    --brown: #6e4a33;
    --brown-light: #7d563c;
    --ink: #1c1410;
    --cream: #fffaf3;
  }
  * { box-sizing: border-box; margin: 0; padding: 0; }
  html, body { width: 1200px; height: 951px; overflow: hidden; }
  body {
    background: var(--page);
    position: relative;
    font-family: "Open Sans", Arial, sans-serif;
  }
  .card {
    position: absolute;
    width: 640px;
    height: 380px;
    background: var(--card);
    border-radius: 22px;
    overflow: hidden;
    box-shadow: 0 6px 18px rgba(40, 25, 15, 0.18);
  }

  /* Front */
  .card-front { left: 90px; top: 60px; }
  .front-band { position: absolute; left: 0; top: 0; width: 640px; height: 380px; }
  .front-logo {
    position: absolute;
    left: 48px;
    top: 70px;
    font-family: "Tinos", "Times New Roman", serif;
    font-weight: 700;
    font-size: 58px;
    line-height: 1.05;
    color: var(--brown);
    letter-spacing: 1px;
  }
  .front-tagline {
    position: absolute;
    right: 26px;
    bottom: 44px;
    font-family: "Tinos", "Times New Roman", serif;
    font-size: 17px;
    color: var(--cream);
    letter-spacing: 0.5px;
    text-transform: uppercase;
  }

  /* Back */
  .card-back { left: 470px; top: 500px; }
  .back-panel {
    position: absolute;
    left: 0; top: 0;
    width: 640px; height: 290px;
    background: linear-gradient(135deg, var(--brown-light) 0%, var(--brown) 45%, var(--brown-dark) 100%);
  }
  .owner-name {
    position: absolute;
    left: 34px; top: 26px;
    font-size: 25px;
    color: var(--cream);
    letter-spacing: 0.3px;
  }
  .owner-title {
    position: absolute;
    left: 34px; top: 62px;
    font-size: 13px;
    color: var(--cream);
  }
  .back-logo {
    position: absolute;
    left: 34px; top: 118px;
    font-family: "Tinos", "Times New Roman", serif;
    font-weight: 700;
    font-size: 40px;
    line-height: 1.05;
    color: var(--cream);
  }
  .product-list {
    position: absolute;
    right: 32px; top: 150px;
    list-style: none;
    text-align: right;
    font-family: "Tinos", "Times New Roman", serif;
    font-size: 17px;
    line-height: 1.2;
    color: var(--cream);
    text-transform: uppercase;
  }
  .contact {
    position: absolute;
    right: 32px; top: 304px;
    list-style: none;
    text-align: right;
    font-size: 17px;
    line-height: 1.55;
    color: var(--ink);
  }
  .contact li { display: flex; justify-content: flex-end; align-items: center; gap: 8px; }
  .contact svg { width: 14px; height: 14px; }
  .web-mark { width: 13px; height: 13px; background: var(--brown-dark); display: inline-block; }
</style>
</head>
<body>

<section class="card card-front" aria-label="Card front">
  <svg class="front-band" viewBox="0 0 640 380" aria-hidden="true">
    <path d="M0 318 Q320 298 640 276 L640 380 L0 380 Z" fill="var(--brown)"/>
  </svg>
  <div class="front-logo">Mill Lane<br>Oven Co</div>
  <p class="front-tagline">Biscuits, cakes, muffins and other sweets</p>
</section>

<section class="card card-back" aria-label="Card back">
  <div class="back-panel"></div>
  <h1 class="owner-name">Peter Alcombe</h1>
  <p class="owner-title">Owner</p>
  <div class="back-logo">Mill Lane<br>Oven Co</div>
  <ul class="product-list">
    <li>Biscuits</li>
    <li>Cakes</li>
    <li>Muffins</li>
    <li>And other sweets</li>
  </ul>
  <ul class="contact">
    <li>555-014-2290
      <svg viewBox="0 0 14 14" aria-hidden="true"><path d="M3 1 L5.5 1 L6.5 4 L5 5.3 Q6.2 8 8.7 9 L10 7.5 L13 8.5 L13 11 Q12 13 10 13 Q2 11 1 4 Q1 2 3 1 Z" fill="var(--ink)"/></svg>
    </li>
    <li>www.millaneoven.example <span class="web-mark" aria-hidden="true"></span></li>
  </ul>
</section>

</body>
</html>
```